Letterhead Design for Law Firm that Specializes in Property Damage Litigation

We are looking for a redesign of our letterhead. Our current letterhead lists all of our current staff members and we'd like to come up with a design that does NOT list all of the staff members so that it does not need to be updated with every newly hired employee. Must be in editable format.

We are a law firm that specializes in property damage, so we need something that is professional, yet modern. The final design should use our existing logo and should use a blue color scheme (alternate colors would be gray, black, and white).

Industry/Entity Type

Legal

Colors
0054AA
0677BA
7BADD7
CADEEF
E8F1F8

```html
<!DOCTYPE html>
<html lang="en">
<head>
<meta charset="utf-8">
<title>Hartwell Crane Moreau Letterhead</title>
<link href="https://fonts.googleapis.com/css2?family=Cinzel:wght@500&family=Montserrat:wght@500;700&family=Barlow:wght@400&family=Lobster&display=swap" rel="stylesheet">
<style>
  :root {
    --brand-blue: #3d5586;
    --text-gray: #555a60;
    --mark-gray: #606266;
    --deco-gray: #dedfe1;
    --deco-blue: #d9dee8;
    --sign-tint: #f1f3f6;
    --backdrop: #e6e6e6;
    --paper: #ffffff;
  }
  * { margin: 0; padding: 0; box-sizing: border-box; }
  html, body { width: 1200px; height: 1200px; overflow: hidden; background: var(--backdrop); }
  .letterhead {
    position: absolute; left: 190px; top: 20px;
    width: 821px; height: 1160px;
    background: var(--paper);
    overflow: hidden;
  }
  .letterhead > * { position: absolute; }

  .brand { left: 103px; top: 92px; display: flex; align-items: center; gap: 14px; }
  .brand-square { width: 22px; height: 22px; background: var(--mark-gray); }
  .brand-name {
    font-family: "Montserrat", sans-serif; font-weight: 700;
    font-size: 21px; letter-spacing: 1.2px;
    color: var(--brand-blue);
  }
  .contact-top {
    left: 540px; top: 82px; width: 180px; text-align: center;
    font-family: "Barlow", sans-serif; font-size: 13px; line-height: 21px; letter-spacing: 1.4px;
    color: var(--brand-blue);
  }
  .letter-date {
    right: 118px; top: 221px;
    font-family: "Montserrat", sans-serif; font-weight: 500; font-size: 13px; letter-spacing: .5px;
    color: var(--brand-blue);
  }
  .letter-headline {
    left: 108px; top: 235px;
    font-family: "Montserrat", sans-serif; font-weight: 700; font-size: 23px; letter-spacing: 1.4px;
    color: var(--brand-blue);
  }
  .letter-body { left: 110px; top: 317px; width: 601px; }
  .letter-body p {
    font-family: Arial, Helvetica, sans-serif; font-size: 12px; line-height: 13.5px;
    text-align: justify; color: var(--text-gray); letter-spacing: -.35px;
    margin-bottom: 27px;
  }

  .office { top: 930px; }
  .office.philadelphia { left: 116px; }
  .office.new-jersey { left: 344px; }
  .office-title {
    font-family: "Cinzel", serif; font-weight: 500; font-size: 16px; letter-spacing: 1px;
    color: var(--brand-blue); margin-bottom: 8px;
  }
  .office-row {
    display: flex; align-items: flex-start; gap: 9px; margin-bottom: 7px;
    font-family: "Barlow", sans-serif; font-size: 12.8px; line-height: 17.4px; letter-spacing: .9px;
    color: var(--text-gray);
  }
  .office-row svg { flex: none; width: 20px; height: 20px; margin-top: -2px; }

  .signer { left: 578px; top: 922px; width: 150px; text-align: center; }
  .signer-name { font-family: "Lobster", cursive; font-size: 21px; color: var(--brand-blue); line-height: 26px; }
  .signer-role { font-family: "Montserrat", sans-serif; font-weight: 500; font-size: 13px; letter-spacing: .6px; color: var(--brand-blue); }
  .signature { left: 565px; top: 990px; width: 145px; height: 62px; background: var(--sign-tint); }

  .corner-accent {
    left: 671px; top: 950px; width: 150px; height: 210px;
    background: linear-gradient(135deg, rgba(255,255,255,0) 45%, var(--deco-blue) 100%);
  }
</style>
</head>
<body>
<main class="letterhead">
  <div class="corner-accent" role="img" aria-label="Soft grey-blue corner accent"></div>

  <div class="brand">
    <div class="brand-square"></div>
    <div class="brand-name">HARTWELL CRANE MOREAU</div>
  </div>

  <div class="contact-top">www.hcmlegal.com<br>(215) 555-0140</div>

  <div class="letter-date">Date: xx / xx / xxxx</div>
  <h1 class="letter-headline">Headline</h1>

  <section class="letter-body">
    <p>Lorem ipsum dolor sit amet, consectetur adipiscing elit, sed do eiusmod tempor incididunt ut labore et dolore magna aliqua. Ut enim ad minim veniam, quis nostrud exercitation ullamco laboris nisi ut aliquip ex ea commodo consequat. velit esse cillum dolore eu fugiat nulla pariatur. Pengecualian sint occaecat cupidatat non proident, sunt in culpa qui officia deserunt mollit anim id est laborum. Lorem ipsum dolor sit amet, consectetur adipiscing elit, sed do eiusmod tempor incididunt ut labore et dolore magna aliqua. Ut enim ad minim veniam, quis nostrud exercitation ullamco laboris nisi ut aliquip ex ea commodo consequat. velit esse cillum dolore eu fugiat nulla pariatur. Pengecualian sint occaecat cupidatat non proident, sunt in culpa qui officia deserunt mollit anim id est laborum. Lorem ipsum dolor sit amet, consectetur adipiscing elit, sed do eiusmod tempor incididunt ut labore et dolore magna aliqua. Ut enim ad minim veniam, quis nostrud exercitation ullamco laboris nisi ut aliquip ex ea commodo consequat. velit esse cillum dolore eu fugiat nulla pariatur. Pengecualian sint occaecat cupidatat non proident, sunt in culpa qui officia deserunt mollit anim id est laborum.</p>
    <p>Lorem ipsum dolor sit amet, consectetur adipiscing elit, sed do eiusmod tempor incididunt ut labore et dolore magna aliqua. Ut enim ad minim veniam, quis nostrud exercitation ullamco laboris nisi ut aliquip ex ea commodo consequat. velit esse cillum dolore eu fugiat nulla pariatur. Pengecualian sint occaecat cupidatat non proident, sunt in culpa qui officia deserunt mollit anim id est laborum. Lorem ipsum dolor sit amet, consectetur adipiscing elit, sed do eiusmod tempor incididunt ut labore et dolore magna aliqua. Ut enim ad minim veniam, quis nostrud exercitation ullamco laboris nisi ut aliquip ex ea commodo consequat. velit esse cillum dolore eu fugiat nulla pariatur. Pengecualian sint occaecat cupidatat non proident, sunt in culpa qui officia deserunt mollit anim id est laborum.</p>
    <p>Lorem ipsum dolor sit amet, consectetur adipiscing elit, sed do eiusmod tempor incididunt ut labore et dolore magna aliqua. Ut enim ad minim veniam, quis nostrud exercitation ullamco laboris nisi ut aliquip ex ea commodo consequat. velit esse cillum dolore eu fugiat nulla pariatur. Pengecualian sint occaecat cupidatat non proident, sunt in culpa qui officia deserunt mollit anim id est laborum. Lorem ipsum dolor sit amet, consectetur adipiscing elit, sed do eiusmod tempor incididunt ut labore et dolore magna aliqua. Ut enim ad minim veniam, quis nostrud exercitation ullamco laboris nisi ut aliquip ex ea commodo consequat. velit esse cillum dolore eu fugiat nulla pariatur. Pengecualian sint occaecat cupidatat non proident, sunt in culpa qui officia deserunt mollit anim id est laborum</p>
    <p>Lorem ipsum dolor sit amet, consectetur adipiscing elit, sed do eiusmod tempor incididunt ut labore et dolore magna aliqua. Ut enim ad minim veniam, quis nostrud exercitation ullamco laboris nisi ut aliquip ex ea commodo consequat. velit esse cillum dolore eu fugiat nulla pariatur. Pengecualian sint occaecat cupidatat non proident, sunt in culpa qui officia deserunt mollit anim id est laborum</p>
  </section>

  <section class="office philadelphia">
    <h2 class="office-title">Philadelphia Office</h2>
    <div class="office-row">
      <svg viewBox="0 0 20 20"><circle cx="10" cy="10" r="10" fill="var(--brand-blue)"/><path d="M6.3 5.2c.5-.4 1.1-.3 1.4.2l1 1.6c.3.5.2 1-.2 1.3l-.6.5c.6 1.3 1.6 2.4 2.9 3l.5-.6c.3-.4.9-.5 1.3-.2l1.6 1c.5.3.6.9.2 1.4l-.7.8c-.5.5-1.3.7-2 .4-2.8-1.1-4.9-3.2-6-6-.3-.7-.1-1.5.4-2z" fill="#fff"/></svg>
      <span>215.555.0140</span>
    </div>
    <div class="office-row">
      <svg viewBox="0 0 20 20"><circle cx="10" cy="10" r="10" fill="var(--brand-blue)"/><rect x="5" y="6" width="10" height="8" rx="1" fill="#fff"/><rect x="7" y="8" width="4" height="1.3" fill="var(--brand-blue)"/><rect x="7" y="10.5" width="4" height="1.3" fill="var(--brand-blue)"/><rect x="12.2" y="8" width="1.5" height="4" fill="var(--brand-blue)"/></svg>
      <span>215.555.0172</span>
    </div>
    <div class="office-row">
      <svg viewBox="0 0 20 20"><circle cx="10" cy="10" r="10" fill="var(--brand-blue)"/><path d="M10 4a4 4 0 0 1 4 4c0 3-4 8-4 8s-4-5-4-8a4 4 0 0 1 4-4z" fill="#fff"/><circle cx="10" cy="8" r="1.6" fill="var(--brand-blue)"/></svg>
      <span>2210 Chestnut Street<br>Suite 840<br>Philadelphia, PA 19103</span>
    </div>
  </section>

  <section class="office new-jersey">
    <h2 class="office-title">New Jersey Office</h2>
    <div class="office-row">
      <svg viewBox="0 0 20 20"><circle cx="10" cy="10" r="10" fill="var(--brand-blue)"/><path d="M6.3 5.2c.5-.4 1.1-.3 1.4.2l1 1.6c.3.5.2 1-.2 1.3l-.6.5c.6 1.3 1.6 2.4 2.9 3l.5-.6c.3-.4.9-.5 1.3-.2l1.6 1c.5.3.6.9.2 1.4l-.7.8c-.5.5-1.3.7-2 .4-2.8-1.1-4.9-3.2-6-6-.3-.7-.1-1.5.4-2z" fill="#fff"/></svg>
      <span>856.555.0193</span>
    </div>
    <div class="office-row">
      <svg viewBox="0 0 20 20"><circle cx="10" cy="10" r="10" fill="var(--brand-blue)"/><rect x="5" y="6" width="10" height="8" rx="1" fill="#fff"/><rect x="7" y="8" width="4" height="1.3" fill="var(--brand-blue)"/><rect x="7" y="10.5" width="4" height="1.3" fill="var(--brand-blue)"/><rect x="12.2" y="8" width="1.5" height="4" fill="var(--brand-blue)"/></svg>
      <span>215.555.0172</span>
    </div>
    <div class="office-row">
      <svg viewBox="0 0 20 20"><circle cx="10" cy="10" r="10" fill="var(--brand-blue)"/><path d="M10 4a4 4 0 0 1 4 4c0 3-4 8-4 8s-4-5-4-8a4 4 0 0 1 4-4z" fill="#fff"/><circle cx="10" cy="8" r="1.6" fill="var(--brand-blue)"/></svg>
      <span>325 Haddon Avenue<br>Suite 310<br>Cherry Hill, NJ 08034</span>
    </div>
  </section>

  <div class="signer">
    <div class="signer-name">Your Name</div>
    <div class="signer-role">LOREM IPSUM</div>
  </div>
  <div class="signature" role="img" aria-label="Handwritten signature of the signing attorney"></div>
</main>
</body>
</html>
```